Proverbs Sermon Series Artwork

We are in need of new artwork for an upcoming sermon series that our Senior Pastor will be preaching for at least the next 6 months. This graphic will be used extensively on our app, website, and in worship services and needs to be of excellent quality and also provide meaning behind the entirety of the series. Proverbs is a very rich book of the Bible that deals with wisdom and how to live according to God's principles. The graphic needs to reflect this truth and communicate to those who see it that there are different ways that each of us can choose to live.
We are very flexible on the goal of this piece and don't really have anything in mind. The graphic that is the most professional but also communicated the goal of the sermon series will be the one selected. Please see the must haves to get an idea of different formats we would like to use this graphic in. It will be a key image in the life of our church over the next 6-12 months.
Thanks for looking into this project. I hope you will submit a graphic design and use your God given talents to help us (and make a little money on the side). ArtBazaarly has served us well in the past and we are excited to use it again.
Updates
As of right now, I have 3 good designs from 2 designers. I would love to see the edits made based on feedback provided. I think there is a lot of potential in all 3 designs. If you have questions please let me know. After all artwork is submitted I will be presenting it to the senior pastor and he will select the one he likes the best. I would like to bring him 5 designs so there is still room for some other good submissions from new designers! Also, I uploaded a road sign image. I would like to see something with an image like that from someone.
Target Market(s)
Church members, app users, website visitors
Industry/Entity Type
Religious
Requirements
Must have
- Artwork must include Proverbs in a bold easy to read font. The graphic must also lend itself to different formats. 1920x1080 wide format graphic, 1024x1024 square icon, 1920x692 banner.
Nice to have
- The sermon series is about us having choices on how to live our lives and the goal that we should take God's way instead of ours. This would lend itself well to road signs or maybe something cool with nature. Maybe even a word art as proverbs is a lot of sayings that speak to wisdom of the Christian walk. I'm pretty flexible.
Should not have
- Not overly feminine like most church artwork. This is geared to the whole body, not women.

```html
<!DOCTYPE html>
<html lang="en">
<head>
<meta charset="utf-8">
<title>Proverbs – Two Ways to Live</title>
<link rel="stylesheet" href="https://fonts.googleapis.com/css2?family=Oswald:wght@300;400&display=swap">
<style>
  :root {
    --sky-top: #e4d9c6;
    --sky-mid: #e9d3a4;
    --haze: #dcc98a;
    --field-top: #8f8f3c;
    --field-bottom: #6e7a2c;
    --title-red: #c2363f;
    --title-shade: #8a2230;
    --ink: #111111;
    --post-light: #8d8f8f;
    --post-dark: #5e6162;
  }
  html, body {
    margin: 0;
    padding: 0;
    width: 1200px;
    height: 675px;
    overflow: hidden;
  }
  .series-art {
    position: relative;
    width: 1200px;
    height: 675px;
    overflow: hidden;
    font-family: "Oswald", "Arial Narrow", sans-serif;
  }
  .landscape {
    position: absolute;
    inset: 0;
    background: linear-gradient(
      to bottom,
      var(--sky-top) 0%,
      var(--sky-mid) 45%,
      var(--haze) 76%,
      var(--field-top) 79%,
      var(--field-bottom) 100%
    );
  }
  .signpost {
    position: absolute;
    left: 770px;
    top: 88px;
    width: 400px;
    height: 587px;
    background: linear-gradient(to right, var(--post-dark), var(--post-light) 50%, var(--post-dark));
    opacity: 0.55;
    border-radius: 6px;
  }
  .title-block {
    position: absolute;
    left: 84px;
    top: 166px;
    display: inline-block;
  }
  .series-title {
    margin: 0;
    font-weight: 400;
    font-size: 155px;
    line-height: 1;
    letter-spacing: 5px;
    margin-right: -5px;
    color: var(--title-red);
    white-space: nowrap;
    text-shadow:
      1px 1px 0 var(--title-shade),
      2px 2px 0 var(--title-shade),
      3px 3px 0 var(--title-shade);
  }
  .title-rule {
    height: 3px;
    width: 100%;
    margin-top: 15px;
    background: var(--title-red);
  }
  .series-subtitle {
    margin: 22px 0 0;
    font-weight: 300;
    font-size: 53px;
    line-height: 1;
    color: var(--ink);
    white-space: nowrap;
  }
</style>
</head>
<body>
  <main class="series-art">
    <div class="landscape" role="img" aria-label="Hazy golden sky over a wide green grassy field"></div>
    <div class="signpost" role="img" aria-label="Weathered wooden signpost with arrows pointing in different directions"></div>
    <div class="title-block">
      <h1 class="series-title">PROVERBS</h1>
      <div class="title-rule"></div>
      <p class="series-subtitle">TWO WAYS TO LIVE</p>
    </div>
  </main>
</body>
</html>
```